Container for chopstick set. Box or cylinder

The package will hold 5 pairs of black chopsticks (see uploaded file). These are the things that we liked from the attached files:
Idea 1: Kraft paper, illustration, the contrast of the green color with black illustration + text and green background
Idea 2: cylinder
Idea 3: Illustration of product, slide opening box type

Target Market(s)

The target market are women with families around between the ages of 25-50.

Font styles to use
Other font styles liked:
• Please see logo

Colors

Designer to choose colors to be used in the design.

Requirements
Must have
• Please incorporate our logo into the package (it's ok to change the colors of our logo), but our logo shouldn't cover a significant surface of the package
• Be creative with color(s).
Nice to have
• Possible designs:
• 1) Cylinder (4cm diameter, 25cm height)
• Alternative A: black matte background
• Alternative B: similar colors in Idea 1 with Kraft paper background.
• 2) Slide opening box (7cm x 25cm x 1cm)
• Alternative C: white box which incorporates our green logo (bottom right)

```html
<!DOCTYPE html>
<html lang="en">
<head>
<meta charset="utf-8">
<title>Kanso Chopsticks – Slide Box Packaging</title>
<link href="https://fonts.googleapis.com/css2?family=Barlow:wght@400;500&display=swap" rel="stylesheet">
<style>
  :root {
    --backdrop: #e2e2e2;
    --box-white: #f7f7f5;
    --box-edge: #d9d9d6;
    --leaf-green: #86b83a;
    --leaf-deep: #5f8a26;
    --ink: #1d1d1d;
    --placeholder-dark: #444444;
  }
  html, body {
    margin: 0;
    padding: 0;
    width: 1200px;
    height: 884px;
    overflow: hidden;
    background: var(--backdrop);
    font-family: "Barlow", "Helvetica Neue", Arial, sans-serif;
    color: var(--ink);
  }
  .canvas {
    position: relative;
    width: 1200px;
    height: 884px;
  }
  .box-lid {
    position: absolute;
    left: 357px;
    top: 357px;
    width: 555px;
    height: 165px;
    background: var(--box-white);
    border: 1px solid var(--box-edge);
    box-sizing: border-box;
  }
  .product-info {
    position: absolute;
    left: 18px;
    top: 77px;
  }
  .product-name {
    margin: 0;
    font-size: 14px;
    line-height: 16px;
    font-weight: 400;
    letter-spacing: 0.1px;
    color: var(--ink);
  }
  .product-tagline {
    margin: 5px 0 0;
    font-size: 7px;
    line-height: 8px;
    font-weight: 500;
    color: var(--ink);
  }
  .product-count {
    margin: 7px 0 0;
    font-size: 5.5px;
    line-height: 6px;
    color: var(--ink);
  }
  .brand-panel {
    position: absolute;
    right: 0;
    top: 0;
    width: 92px;
    height: 100%;
    background: var(--leaf-green);
  }
  .brand-dot {
    position: absolute;
    left: 34px;
    top: 25px;
    width: 24px;
    height: 24px;
    border-radius: 50%;
    background: var(--leaf-deep);
  }
  .brand-name {
    position: absolute;
    left: 0;
    width: 100%;
    top: 55px;
    text-align: center;
    font-size: 12px;
    line-height: 14px;
    font-weight: 500;
    color: var(--ink);
  }
  .box-side {
    position: absolute;
    left: 258px;
    top: 590px;
    width: 570px;
    height: 42px;
    background: var(--box-white);
    border: 1px solid var(--box-edge);
    box-sizing: border-box;
  }
  .side-accent {
    position: absolute;
    right: 0;
    top: 0;
    width: 96px;
    height: 5px;
    background: var(--leaf-green);
  }
  .chopstick-artwork {
    position: absolute;
    left: 27px;
    top: 17px;
    width: 516px;
    height: 10px;
    border-radius: 5px;
    background: linear-gradient(90deg, var(--placeholder-dark), #555555);
  }
</style>
</head>
<body>
<main class="canvas">
  <section class="box-lid" aria-label="Box lid">
    <div class="product-info">
      <h1 class="product-name">Kanso Chopsticks</h1>
      <p class="product-tagline">Traditionally-crafted Reusable<br>Japanese Chopsticks</p>
      <p class="product-count">set of 5</p>
    </div>
    <div class="brand-panel">
      <span class="brand-dot"></span>
      <span class="brand-name">sprigwell</span>
    </div>
  </section>

  <section class="box-side" aria-label="Box side panel">
    <span class="side-accent"></span>
    <div class="chopstick-artwork" role="img" aria-label="Illustration of a black chopstick running along the side panel"></div>
  </section>
</main>
</body>
</html>
```